Unique Brovek Building Bussiness Card Design

www.brovek.com.au

Please see website for Company profile. We require a design that incorporates our logo colours and is unique in shape and style compared to all other business cards.

www.brovek.com.au

INSPIRE US !!!
Updates

Target Market(s)

Facility managers, Building Managers, Architects

Industry/Entity Type

Business

Contact Information for Business Card

Brovek Property Works
Project Manager
Dalton Pryseworth
0437 916 248
Sales@brovek.com.au

Logo Text

Brovek Property Works

Logo styles of interest
Abstract Logo
Requirements
Nice to have
• Card must show we are an established big business to trust.

```html
<!DOCTYPE html>
<html lang="en">
<head>
<meta charset="utf-8">
<title>Brovek Property Works – Business Card Concepts</title>
<link href="https://fonts.googleapis.com/css2?family=Arvo:wght@700&family=Open+Sans:wght@400;700&family=Questrial&family=Alegreya:wght@700&family=Tinos&display=swap" rel="stylesheet">
<style>
  :root {
    --page: #ffffff;
    --ink: #111111;
    --navy: #1d4a73;
    --red: #b51206;
    --orange: #e8620a;
    --blue-frame: #1f5f8b;
    --card-edge: #3a3a3a;
  }
  * { margin: 0; padding: 0; box-sizing: border-box; }
  html, body { width: 1200px; height: 741px; overflow: hidden; background: var(--page); }
  .canvas { position: relative; width: 1200px; height: 741px; }

  .card {
    position: absolute; width: 414px; height: 253px;
    background: #fff; border: 1px solid var(--card-edge); overflow: hidden;
  }
  .card--band      { left: 101px; top: 80px; }
  .card--gradient  { left: 660px; top: 80px; }
  .card--split     { left: 110px; top: 423px; }
  .card--framed    { left: 645px; top: 428px; border: 5px solid var(--red); }

  .brand {
    position: absolute; left: 36px; top: 42px;
    display: flex; align-items: center; gap: 8px;
  }
  .brand__square { width: 26px; height: 26px; background: var(--orange); }
  .brand__name {
    font-family: 'Arvo', serif; font-weight: 700; font-size: 30px;
    color: var(--navy); letter-spacing: 0.2px;
  }

  .name-sans { font-family: 'Questrial', sans-serif; font-size: 18px; font-weight: 700; }
  .role-serif { font-family: 'Alegreya', serif; font-weight: 700; font-size: 15px; }
  .contact { font-family: 'Tinos', serif; font-size: 17px; line-height: 23px; white-space: pre; }

  /* card 1 */
  .band-red { position: absolute; left: 0; top: 112px; width: 100%; height: 9px; background: var(--red); }
  .band-orange { position: absolute; left: 0; top: 122px; width: 100%; height: 4px; background: var(--orange); }
  .card--band .details { position: absolute; left: 40px; top: 141px; }
  .card--band .person__name { font-family: 'Open Sans', sans-serif; font-weight: 700; font-size: 15.5px; color: var(--red); line-height: 19px; }
  .card--band .person__role { font-family: 'Open Sans', sans-serif; font-size: 15.5px; color: var(--ink); line-height: 19px; }
  .card--band .contact { color: var(--ink); font-size: 18px; line-height: 23px; margin-top: 2px; }

  /* card 2 */
  .panel-gradient {
    position: absolute; left: 0; top: 123px; width: 100%; height: 130px;
    background: linear-gradient(90deg, var(--orange) 0%, #dd4a08 50%, var(--red) 100%);
  }
  .card--gradient .details { position: absolute; left: 40px; top: 133px; color: #fff; }
  .card--gradient .contact { margin-top: 9px; }

  /* card 3 */
  .panel-left { position: absolute; left: 0; top: 122px; width: 207px; height: 131px; background: var(--orange); }
  .panel-right { position: absolute; left: 207px; top: 122px; width: 207px; height: 131px; background: var(--red); }
  .card--split .contact { position: absolute; left: 17px; top: 167px; color: #fff; font-size: 14.5px; line-height: 19px; }
  .card--split .person { position: absolute; left: 240px; top: 170px; color: #fff; }
  .card--split .name-sans { font-size: 20px; }
  .card--split .role-serif { font-size: 16.5px; margin-left: 4px; }

  /* card 4 */
  .inner-frame { position: absolute; inset: 4px; border: 2px solid var(--blue-frame); }
  .card--framed .brand { left: 34px; top: 38px; }
  .card--framed .details { position: absolute; left: 48px; top: 117px; color: var(--ink); }
  .card--framed .contact { margin-top: 9px; }
</style>
</head>
<body>
<main class="canvas">

  <section class="card card--band">
    <div class="brand"><span class="brand__square"></span><span class="brand__name">brovek.com.au</span></div>
    <div class="band-red"></div>
    <div class="band-orange"></div>
    <div class="details">
      <p class="person__name">Dalton Pryseworth</p>
      <p class="person__role">Project Manager</p>
      <p class="contact">Email  :   Sales@brovek.com.au
Phone  :   0437 916 248</p>
    </div>
  </section>

  <section class="card card--gradient">
    <div class="brand"><span class="brand__square"></span><span class="brand__name">brovek.com.au</span></div>
    <div class="panel-gradient"></div>
    <div class="details">
      <p class="name-sans">Dalton Pryseworth</p>
      <p class="role-serif">Project Manager</p>
      <p class="contact">Email  :   Sales@brovek.com.au
Phone  :   0437 916 248</p>
    </div>
  </section>

  <section class="card card--split">
    <div class="brand"><span class="brand__square"></span><span class="brand__name">brovek.com.au</span></div>
    <div class="panel-left"></div>
    <div class="panel-right"></div>
    <p class="contact">Email  :   Sales@brovek.com.au
Phone  :   0437 916 248</p>
    <div class="person">
      <p class="name-sans">Dalton Pryseworth</p>
      <p class="role-serif">Project Manager</p>
    </div>
  </section>

  <section class="card card--framed">
    <div class="inner-frame"></div>
    <div class="brand"><span class="brand__square"></span><span class="brand__name">brovek.com.au</span></div>
    <div class="details">
      <p class="name-sans">Dalton Pryseworth</p>
      <p class="role-serif">Project Manager</p>
      <p class="contact">Email  :   Sales@brovek.com.au
Phone  :   0437 916 248</p>
    </div>
  </section>

</main>
</body>
</html>
```